New Website for Asia Travel Agency

Lanternpath Journeys Website

We want a redesign for our current website, www.lanternpathjourneys.example. We want you to get creative with our brand and present our company in a unique, creative and compelling way, that communicates our exotic destinations and tours, the local and authentic character of our travel consultants and the trustworthy and professional nature of our company.

Who is this company?

Lanternpath Journeys is an online tour operator specializing in providing tailor-made tours to eight destinations in Asia; Vietnam, Thailand, Laos, Cambodia, Indonesia, Myanmar, Japan and China. They were launched in mid February 2012 with headquarters in Bangkok, Thailand, and staffed by locals and expats with many years of experience in the travel industry, and who are committed to sharing their deep knowledge of, and passion for the region.

Local knowledge

Our consultants at Lanternpath Journeys are all locals – they know their destinations inside-out and draw upon invaluable first-hand experience and information when planning your tour. They have insights into local culture and tradition, they know the best places to visit, the most worthwhile experiences to have and, most importantly, they have the knowledge to create exactly the holiday you desire.

All hotels and activities featured in a Lanternpath Journeys tour are regularly inspected by our consultants to ensure the highest quality standards are met and that all information is correct and up to date.

Unforgettable Travel Experiences

Whether it's a cultural exploration or a beach holiday you're after – or a mix of both – Lanternpath Journeys has an itinerary for you – and if we don't have one, we'll tailor-make one! From the main sights to remote villages, our locally based Travel Specialists will give you unique insights into every place you visit and let you delve into known destinations from new perspectives.

Our tours offer a variety of hotel and resort options, premium stays in deluxe accommodation, heritage hotels, a five-star boutique or on the water in a junk. Tap into our experience let us create an experience unique to you – and one you will never forget.

What type of Holiday to Asia?

Our itineraries at Lanternpath Journeys are created according to different inspirations. Some travelers are interested in the History & Culture of a destination, while some like to stay active with Adventure tours. A Cross Border trip explores different countries in a single tour, while Velvet Summit tours offer the highest level of exclusivity across our destinations. There are 14 different Holiday Types to choose from, or you can mix and match ideas to create your dream vacation.

Target Market(s)

Slightly more female, aged 30-65, are creative, professional and looking for something different, something a bit unusual.

Industry/Entity Type

Boutique

Requirements
Must have
• 5 page designs:

1. Homepage
2. Tours list page for a country
3. Tour page
4. 'Be Inspired' page
5. Country page
6. Enquiry page

Our inspirations.

The following list shows websites we love and which inspire us... to give you some indication of our preferred styles, functions and layouts:

http://www.frostmeridian.example/en/ (we really like this, great personality, like the use of icons for tour types)
http://www.pebblewalks.example.uk/ (very simple design elements and layout)
http://www.sunvalecoast.example/ (great use of background image, nice simple nav bar)
http://www.roamcedarfall.example/ (we like because it has distinct personality and is well suited to the destination)
http://www.seemarlowton.example/ (clear personality through font use)
http://www.vastroving.example/ (original, unique)
http://www.wanderquill.example/long-loop-of-asia (like the map style)

Key design points:

1. You must use our existing logo (attached), but you can change the color scheme of the logo to accord with the whichever color scheme you choose for the main designs.
2. Our logo strapline is "Asia is our Lanternpath" and should be used prominently on the page to reinforce the meaning of our company name.
3. Home page and tours list pages should allow the user to see the choice of tours immediately without scrolling & Introduction copy should be minimal.
4. We and our site visitors are inspired and excited by our photography, this is an element of the site which we would like to maintain and build on, though the section page header sliders are currently too big and do not allow quick access to the section content. This is a design problem which needs a solution. Full page photographic backgrounds may be an answer?
5. Tour page should display other contextual tours, from the same country or style/type
6. We should promote press coverage in various places
7. We should display consultant profiles in various places
8. Map designs for tour page and country page, plus a modal pop out for the home page. These are complex and may have a few small photos and short descriptive text only, though this is limited by your own creativity. We will use graphics and html5/css3 so there are no creative limitations.
9. The 'Inspirations' / 'Be Inspired' page is for people who want travel and holiday ideas, who are looking for inspiration on where to go and what to do. This section needs to reflect the exotic, the unusual, the extraordinary in our destinations and tours, and we leave this to your creative genius to develop. We are also interested in how this inspirations page is related to the blog and social media content we produce daily, is there an integration here? Can we present YouTube videos, our blog posts, Facebook posts etc, on this page? This is another design challenge.
10. We would like to see designs for the tours list page which feature AJAX content filtering (for instance: http://demo.layoutbrisk.example/?acn), we would like to see how to include this type of content filtering on homepage and destination page also.
11. The 'Enquiry' call to action should be on all pages and prominent.
12. The enquiry page can reflect the same fields as the existing website enquiry page

Values to be communicated:

- Exotic: Asia is exotic, and our tours will expose clients to extraordinary sights and unusual cultural encounters.
- Authentic: Our travel consultants all live in the destinations themselves, they are local nationals and have all the insider knowledge to give clients a truly authentic experience of our destinations
- Unique: All of our tours are tailor made, there are no fixed departure dates or join-in groups. All tour itineraries can be uniquely designed for our clients, from departure dates to destinations.
- Trust: Some travelers prefer to book their holidays with local agencies they can meet in person, rather than with online companies like us who live in the destinations and who they only get to meet on Skype video or phone. We want to convey that we are trustworthy. We have attempted this through presenting a 'meet the team' page and a 'press' page and advert, as well as offering a prominent international phone number. How we you build on this and further convey this value?

```html
<!DOCTYPE html>
<html lang="en">
<head>
<meta charset="utf-8">
<title>Lanternpath Journeys — Home</title>
<link href="https://fonts.googleapis.com/css2?family=Montserrat:wght@400;500;600;700&family=Arimo:wght@400;700&display=swap" rel="stylesheet">
<style>
:root{
  --red:#d50d0d;
  --red-dark:#b10808;
  --ink:#333333;
  --ink-soft:#555555;
  --charcoal:#2f2e2e;
  --charcoal-deep:#262525;
  --panel:#373636;
  --mist:#dcecec;
  --sage:#bcd3d1;
  --line:#e3e3e3;
  --white:#ffffff;
}
*{box-sizing:border-box;margin:0;padding:0}
html,body{width:1060px;height:1200px;overflow:hidden}
body{position:relative;background:var(--white);font-family:"Arimo",Arial,sans-serif;color:var(--ink)}
.abs{position:absolute}

/* hero */
.hero-photo{left:0;top:0;width:1060px;height:636px;
  background:linear-gradient(90deg,#5d5a50 0%,#77756a 14%,#3f5a2d 30%,#4f7a34 48%,#3b6a2a 62%,#6f6c60 80%,#57544b 100%)}
.nav{left:176px;top:32px;width:708px;height:42px;background:var(--white);display:flex;box-shadow:0 2px 3px rgba(0,0,0,.25)}
.brand{width:222px;display:flex;align-items:center;padding-left:12px;gap:8px}
.brand-mark{width:26px;height:26px;background:var(--sage);border:2px solid #555}
.brand-text{font-family:"Montserrat",Arial,sans-serif}
.brand-name{font-size:14px;font-weight:600;color:var(--ink);letter-spacing:-.3px;white-space:nowrap}
.brand-tag{font-size:7px;color:var(--ink-soft);margin-top:1px}
.menu{display:flex;list-style:none}
.menu li{font-family:"Montserrat",Arial,sans-serif;font-size:9.5px;color:#555;display:flex;align-items:center;justify-content:center;border-left:1px solid #e6e6e6;text-transform:uppercase;white-space:nowrap}
.menu li.active{background:var(--red);color:var(--white);border-left:none}

.hero-title{left:216px;top:372px;height:52px;width:444px;background:rgba(30,30,30,.88);clip-path:polygon(0 0,100% 0,92% 100%,0 100%);
  color:var(--white);font-family:"Montserrat",Arial,sans-serif;font-weight:500;font-size:37px;line-height:52px;padding-left:10px;letter-spacing:.3px;white-space:nowrap}
.hero-sub{left:216px;top:424px;height:27px;width:372px;background:var(--red);clip-path:polygon(0 0,100% 0,94% 100%,0 100%);
  color:var(--white);font-family:"Montserrat",Arial,sans-serif;font-weight:500;font-size:14px;letter-spacing:-.2px;line-height:27px;padding-left:9px;white-space:nowrap}

/* search */
.search-band{left:177px;top:521px;width:707px;height:115px;background:linear-gradient(#dcecec,#eef6f6)}
.tab{top:534px;height:24px;font-family:"Montserrat",Arial,sans-serif;font-weight:600;font-size:12px;color:var(--white);text-align:center;line-height:26px}
.tab-tours{left:189px;width:76px;background:var(--panel)}
.tab-hotel{left:268px;width:75px;background:var(--red)}
.search-box{left:189px;top:558px;width:473px;height:92px;background:var(--panel);box-shadow:0 6px 6px -4px rgba(0,0,0,.3)}
.select{top:570px;height:28px;background:var(--white);border:1px solid #ccc;font-size:12px;color:#aaa;padding-left:12px;line-height:27px}
.select svg{position:absolute;right:5px;top:5px}
.btn-search{left:198px;top:608px;width:82px;height:28px;background:var(--red);color:var(--white);font-family:"Montserrat",Arial,sans-serif;font-weight:600;font-size:12px;text-align:center;line-height:28px;box-shadow:0 2px 0 var(--red-dark)}
.adv-link{left:289px;top:617px;font-family:"Montserrat",Arial,sans-serif;font-size:9px;color:var(--white);text-decoration:underline}
.btn-explore{left:511px;top:608px;width:141px;height:28px;background:var(--sage);color:var(--charcoal);font-family:"Montserrat",Arial,sans-serif;font-weight:600;font-size:13px;display:flex;align-items:center;justify-content:center;gap:6px;box-shadow:0 2px 0 #8fa8a6;white-space:nowrap}

.offer{left:674px;top:534px;width:198px;height:116px;background:var(--red);overflow:hidden;box-shadow:0 4px 5px -3px rgba(0,0,0,.35)}
.offer-photo{position:absolute;left:80px;top:0;width:118px;height:116px;background:linear-gradient(160deg,#31425f 0%,#1d2740 55%,#6b4a36 100%)}
.offer-kicker{position:absolute;left:8px;top:8px;font-family:"Montserrat",Arial,sans-serif;font-weight:700;font-size:13px;line-height:13px;color:var(--white)}
.offer-kicker span{color:#7d0707}
.offer-visit{position:absolute;left:8px;top:69px;font-family:"Montserrat",Arial,sans-serif;font-weight:700;font-size:18px;color:var(--white);line-height:18px}
.offer-city{position:absolute;left:8px;top:86px;font-family:"Montserrat",Arial,sans-serif;font-weight:700;font-size:25px;color:var(--white);line-height:26px;letter-spacing:-.3px}

/* intro */
.intro-title{left:188px;top:670px;font-family:"Montserrat",Arial,sans-serif;font-size:24px;font-weight:500;color:var(--ink);letter-spacing:-.5px;white-space:nowrap}
.intro-title span{color:var(--red)}
.intro-copy{left:189px;top:704px;width:530px;font-size:9px;line-height:12px;color:#444}
.more{font-family:"Montserrat",Arial,sans-serif;font-size:12px;color:#444;display:flex;align-items:center;gap:2px}
.more span{color:var(--red)}
.asia-map{left:740px;top:664px;width:136px;height:100px;background:radial-gradient(ellipse at 50% 45%,#cfcfcf 0%,#dcdcdc 55%,rgba(255,255,255,0) 72%)}
.divider{left:170px;top:783px;width:720px;height:2px;background:linear-gradient(90deg,rgba(0,0,0,0),#e4e4e4 15%,#e4e4e4 85%,rgba(0,0,0,0))}

/* columns */
.col-title{top:802px;font-family:"Montserrat",Arial,sans-serif;font-weight:700;font-size:15px;color:var(--ink);letter-spacing:-.4px;white-space:nowrap}
.col-title span{color:var(--red)}
.col-rule{top:815px;width:1px;height:133px;background:var(--line)}
.team-photo{top:827px;width:70px;height:91px}
.news-date{left:423px;top:828px;font-family:"Montserrat",Arial,sans-serif;font-size:16px;color:#bdbdbd}
.news-head{left:423px;top:848px;width:215px;font-family:"Montserrat",Arial,sans-serif;font-weight:600;font-size:10.5px;line-height:14px;color:var(--red)}
.news-copy{left:423px;top:877px;width:215px;font-size:9px;line-height:12px;color:#444}
.quote-head{left:658px;top:829px;font-family:"Montserrat",Arial,sans-serif;font-weight:600;font-size:10.5px;color:var(--red)}
.quote-mark{left:657px;top:842px;font-family:Georgia,serif;font-size:26px;color:#c8c8c8;line-height:26px}
.quote-copy{left:668px;top:850px;width:200px;font-size:9px;line-height:12px;color:#444}
.quote-copy i{font-family:Georgia,serif;color:#c8c8c8;font-style:normal}
.quote-name{left:657px;top:894px;font-family:"Montserrat",Arial,sans-serif;font-weight:600;font-size:10.5px;color:var(--ink)}

/* footer */
.footer{left:0;top:957px;width:1060px;height:197px;background:var(--charcoal)}
.foot-title{top:985px;font-family:"Montserrat",Arial,sans-serif;font-weight:600;font-size:10.5px;letter-spacing:-.2px;color:var(--white);white-space:nowrap}
.foot-list{top:1006px;list-style:none;font-size:9.5px;line-height:14px;color:#dcdcdc}
.foot-rule{top:986px;width:0;height:142px;border-left:1px dotted #555}
.sub-copy{left:636px;top:1006px;width:250px;font-size:8.5px;line-height:12.5px;color:#dcdcdc}
.sub-field{left:636px;top:1038px;width:248px;height:30px;background:var(--white);border-radius:2px;font-size:9px;color:#999;padding-left:10px;line-height:30px}
.sub-btn{left:778px;top:1078px;width:106px;height:29px;background:var(--sage);border-radius:2px;box-shadow:0 2px 0 #8fa8a6;font-family:"Montserrat",Arial,sans-serif;font-weight:600;font-size:12px;color:var(--charcoal);text-align:center;line-height:29px}
.bottom-bar{left:0;top:1154px;width:1060px;height:46px;background:var(--charcoal-deep)}
.legal{top:1172px;font-size:8px;color:#777;white-space:nowrap}
</style>
</head>
<body>

<div class="abs hero-photo" role="img" aria-label="Photograph of two young children among carved stone temple guardians decorated with red flowers in Bali"></div>

<header class="abs nav">
  <div class="brand">
    <div class="brand-mark"></div>
    <div class="brand-text">
      <div class="brand-name">Lanternpath Journeys</div>
      <div class="brand-tag">Asia is our Lanternpath.</div>
    </div>
  </div>
  <ul class="menu">
    <li class="active" style="width:52px">Home</li>
    <li style="width:88px">Destinations</li>
    <li style="width:54px">Tours</li>
    <li style="width:91px">Holiday Types</li>
    <li style="width:76px">Best Value</li>
    <li style="width:70px">About Us</li>
    <li style="width:55px">Blog</li>
  </ul>
</header>

<h1 class="abs hero-title">FAMILY FUN IN BALI</h1>
<p class="abs hero-sub">FOUR WHEEL DRIVES, FARMING AND MORE</p>

<div class="abs search-band"></div>
<div class="abs tab tab-tours">TOURS</div>
<div class="abs tab tab-hotel">HOTEL</div>
<div class="abs search-box"></div>
<div class="abs select" style="left:198px;width:147px">All Countries
  <svg width="19" height="18" viewBox="0 0 19 18"><rect width="19" height="18" rx="2" fill="#373636"/><path d="M5 7l4.5 4.5L14 7" stroke="#fff" stroke-width="1.8" fill="none"/></svg></div>
<div class="abs select" style="left:351px;width:147px">All Cities
  <svg width="19" height="18" viewBox="0 0 19 18"><rect width="19" height="18" rx="2" fill="#373636"/><path d="M5 7l4.5 4.5L14 7" stroke="#fff" stroke-width="1.8" fill="none"/></svg></div>
<div class="abs select" style="left:504px;width:148px">All Durations
  <svg width="19" height="18" viewBox="0 0 19 18"><rect width="19" height="18" rx="2" fill="#373636"/><path d="M5 7l4.5 4.5L14 7" stroke="#fff" stroke-width="1.8" fill="none"/></svg></div>
<div class="abs btn-search">SEARCH</div>
<div class="abs adv-link">ADVANCED SEARCH</div>
<div class="abs btn-explore">
  <svg width="16" height="16" viewBox="0 0 16 16"><circle cx="8" cy="8" r="6.5" stroke="#2f2e2e" stroke-width="1.6" fill="none"/><path d="M10.8 5.2L9 9 5.2 10.8 7 7z" fill="#2f2e2e"/></svg>
  EXPLORE ASIA
</div>

<div class="abs offer">
  <div class="offer-photo" role="img" aria-label="Photograph of a Singapore skyline with a rooftop hotel at dusk"></div>
  <div class="offer-kicker"><span>SPECIAL</span><br>OFFER</div>
  <div class="offer-visit">VISIT</div>
  <div class="offer-city">SINGAPORE</div>
</div>

<h2 class="abs intro-title"><span>ASIA</span> IS OUR LANTERNPATH</h2>
<p class="abs intro-copy">No one knows a destination better than someone who lives, works and plays there. That's the foundation of Lanternpath Journeys. Our travel specialists reside in Asia. They live Asia, they breathe Asia. And they're intrigued explorers as much as they are citizens of Bangkok, or Bali, or Luang Prabang.</p>
<div class="abs more" style="left:188px;top:745px;font-size:14px">
  <svg width="14" height="10" viewBox="0 0 14 10"><path d="M1 1l4 4-4 4M6 1l4 4-4 4" stroke="#333" stroke-width="1.3" fill="none"/></svg><span>Read</span> More</div>
<div class="abs asia-map" role="img" aria-label="Grey map of Asia"></div>
<div class="abs divider"></div>

<h3 class="abs col-title" style="left:188px"><span>MEET</span> OUR TEAM</h3>
<div class="abs team-photo" style="left:187px;background:linear-gradient(#8a8f7a,#c9c3b6)" role="img" aria-label="Photo of a travel consultant"></div>
<div class="abs team-photo" style="left:261px;background:linear-gradient(#5ab2d8,#d8d2c2)" role="img" aria-label="Photo of a travel consultant at the beach"></div>
<div class="abs team-photo" style="left:334px;background:linear-gradient(#c0241a,#3a2a2a)" role="img" aria-label="Photo of a travel consultant in front of red lanterns"></div>
<div class="abs more" style="left:188px;top:925px">
  <svg width="12" height="9" viewBox="0 0 14 10"><path d="M1 1l4 4-4 4M6 1l4 4-4 4" stroke="#333" stroke-width="1.3" fill="none"/></svg><span>Read</span> More</div>

<div class="abs col-rule" style="left:412px"></div>
<h3 class="abs col-title" style="left:423px"><span>LATEST</span> NEWS</h3>
<div class="abs news-date">26/12/2013</div>
<div class="abs news-head">Vietnam - A Travel Destination Ideal for Photography</div>
<p class="abs news-copy">Lorem ipsum dolor sit amet, consectetuer adipiscing elit, sed diam nonummy nibh euismod tincidunt ut laoreet dolore magna aliquam.</p>
<div class="abs more" style="left:423px;top:925px">
  <svg width="12" height="9" viewBox="0 0 14 10"><path d="M1 1l4 4-4 4M6 1l4 4-4 4" stroke="#333" stroke-width="1.3" fill="none"/></svg><span>Read</span> More</div>

<div class="abs col-rule" style="left:646px"></div>
<h3 class="abs col-title" style="left:657px"><span>TESTIMONIALS</span></h3>
<div class="abs quote-head">An itinerary Just right</div>
<div class="abs quote-mark">&ldquo;</div>
<p class="abs quote-copy">We had a great trip. Thank you so much for all the preparation work to get the itinerary just right. <i>&rdquo;</i></p>
<div class="abs quote-name">Maren Eastwick</div>
<div class="abs more" style="left:657px;top:925px">
  <svg width="12" height="9" viewBox="0 0 14 10"><path d="M1 1l4 4-4 4M6 1l4 4-4 4" stroke="#333" stroke-width="1.3" fill="none"/></svg><span>View</span> More</div>

<footer class="abs footer"></footer>
<h4 class="abs foot-title" style="left:178px">QUICK LINKS</h4>
<ul class="abs foot-list" style="left:177px">
  <li>Home</li><li>Destinations</li><li>Tours</li><li>Holiday Types</li><li>Best Value</li><li>About Us</li><li>Blog</li>
</ul>
<div class="abs foot-rule" style="left:274px"></div>
<h4 class="abs foot-title" style="left:294px">OUR LANTERNPATH</h4>
<ul class="abs foot-list" style="left:294px">
  <li>Thailand</li><li>Indonesia</li><li>Laos</li><li>Cambodia</li><li>Japan</li><li>Myanmar</li><li>Vietnam</li><li>China</li><li>Multi-country</li>
</ul>
<div class="abs foot-rule" style="left:413px"></div>
<h4 class="abs foot-title" style="left:433px">ABOUT LANTERNPATH JOURNEYS</h4>
<ul class="abs foot-list" style="left:434px">
  <li>Why Book With Us</li><li>About Us</li><li>Meet The Team</li><li>Careers</li><li>In The Press</li><li>Affiliate Program</li>
</ul>
<div class="abs foot-rule" style="left:616px"></div>
<h4 class="abs foot-title" style="left:636px">SUBSCRIBE TO OUR E-NEWSLETTER</h4>
<p class="abs sub-copy">Sign up for Lanternpath Journeys' e-newsletter featuring promotions, travel musings and insider destination.</p>
<div class="abs sub-field">Email Address</div>
<div class="abs sub-btn">SUBSCRIBE</div>

<div class="abs bottom-bar"></div>
<div class="abs legal" style="left:177px">Contact Us &nbsp;|&nbsp; Terms</div>
<div class="abs legal" style="right:176px">&copy; 2013 Lanternpath Journeys. All Rights Reserved</div>

</body>
</html>
```